Health Coaching Flyer for New Clients

I need a two-sided flyer (3.5" x 8.5" preferred or 5" x 7") to distribute to potential coaching clients. My business name is Talvora Health & Wellness Coaching. My business is focused on helping people with habit changes that contribute to their overall well-being. I would like the design colors to be gender neutral. I would like a small photo of myself near the "my name is Jen" statement. Please feel free to change the logo color to match the design.

Target Market(s)

Adults of all ages.

Font styles to use
Serif

Requirements
Must have
• Emphasize my opening question (found in health coaching brochure - attached).
• Small picture of myself near "my name is Jen" statement.
Should not have
• No light of pastel colors.

```html
<!DOCTYPE html>
<html lang="en">
<head>
<meta charset="utf-8">
<title>Talvora Health &amp; Wellness Coaching – Flyer</title>
<link rel="stylesheet" href="https://fonts.googleapis.com/css2?family=Advent+Pro:wght@400;500;600&family=Dancing+Script:wght@500&display=swap">
<style>
  :root{
    --page:#e4e5e7;
    --panel:#333333;
    --panel-soft:#3b3b3b;
    --ink-light:#f2f2f2;
    --ink-dark:#2e2e2e;
    --band:#ffffff;
    --food-a:#a9b5bb;
    --food-b:#7f8c92;
    --fit-a:#3fb7e6;
    --fit-b:#9acb3c;
    --portrait-a:#8a6d5c;
    --portrait-b:#4d3a31;
  }
  *{box-sizing:border-box;margin:0;padding:0}
  html,body{width:1200px;height:1162px;overflow:hidden}
  body{background:var(--page);font-family:"Advent Pro",sans-serif;color:var(--ink-light);position:relative}
  .flyer{position:absolute;top:112px;width:384px;height:934px;background:var(--panel);overflow:hidden}
  .flyer--front{left:206px}
  .flyer--back{left:610px;background:var(--panel-soft)}

  .brand{position:absolute;left:30px;width:324px;text-align:left}
  .brand__name{display:block;font-weight:600;font-size:50px;letter-spacing:6px;line-height:1;color:var(--ink-light)}
  .brand__tag{display:block;font-weight:600;font-size:13.5px;letter-spacing:.2px;margin-top:4px;color:var(--ink-light)}
  .flyer--front .brand{top:22px}
  .flyer--back .brand{top:850px;left:28px}

  .hero{position:absolute;left:0;top:0;width:384px;height:470px;
    background:linear-gradient(135deg,var(--food-a),#c7d0d4 60%,var(--food-b));
    clip-path:polygon(0 128px,384px 104px,384px 432px,0 466px)}
  .hero__question{position:absolute;left:210px;top:130px;width:156px;text-align:center;
    font-family:"Dancing Script",cursive;font-size:30px;line-height:42px;color:var(--ink-dark)}

  .portrait{position:absolute;left:66px;top:436px;width:256px;height:256px;border-radius:50%;
    border:4px solid #fff;background:radial-gradient(circle at 50% 40%,var(--portrait-a),var(--portrait-b))}

  .intro__title{position:absolute;top:704px;left:0;width:384px;text-align:center;font-size:31px;font-weight:500}
  .intro__body{position:absolute;top:746px;left:30px;width:324px;text-align:center;font-size:15.5px;line-height:20.2px}

  .backdrop{position:absolute;left:40px;top:60px;width:300px;height:300px;border-radius:50%;
    background:radial-gradient(circle,rgba(120,90,70,.28),rgba(60,60,60,0) 70%)}
  .benefits__title{position:absolute;left:37px;top:36px;font-size:31px;font-weight:500;white-space:nowrap}
  .benefits__list{list-style:none;position:absolute;left:38px;top:91px;width:330px}
  .benefits__item{position:relative;padding-left:40px;font-size:15px;line-height:18.4px}
  .benefits__item svg{position:absolute;left:0;top:0;width:22px;height:22px}
  .benefits__item:nth-child(1){margin-bottom:18px}
  .benefits__item:nth-child(2){margin-bottom:18px}
  .benefits__item:nth-child(3){margin-bottom:17px}
  .benefits__item:nth-child(4){margin-bottom:18px}

  .fitness{position:absolute;left:0;top:360px;width:384px;height:340px;
    background:linear-gradient(160deg,var(--fit-b) 0%,#6ccde0 35%,var(--fit-a) 70%,#2a9fd0 100%);
    clip-path:polygon(0 72px,384px 8px,384px 268px,0 332px)}
  .invite{position:absolute;left:24px;top:520px;width:340px;transform:rotate(-10deg);
    font-family:"Dancing Script",cursive;font-size:14px;line-height:18px;color:var(--ink-dark);text-align:center}
  .invite p+p{margin-top:12px}

  .contact__lead{position:absolute;right:23px;top:667px;text-align:right;font-size:18px;line-height:22px}
  .contact__band{position:absolute;left:0;top:748px;width:384px;height:86px;background:var(--band);color:var(--ink-dark);text-align:center}
  .contact__name{font-size:44px;font-weight:500;letter-spacing:1px;line-height:1;margin-top:8px}
  .contact__line{font-size:19px;margin-top:4px}
</style>
</head>
<body>
  <section class="flyer flyer--front">
    <div class="brand">
      <span class="brand__name">TALVORA</span>
      <span class="brand__tag">HEALTH &amp; WELLNESS COACHING</span>
    </div>
    <div class="hero" role="img" aria-label="Photo of a heart-shaped plate with fruit, nuts and grains beside a stethoscope on wooden boards"></div>
    <p class="hero__question">Need support in making real, lasting lifestyle and behavior changes?</p>
    <div class="portrait" role="img" aria-label="Portrait photo of Jen"></div>
    <h2 class="intro__title">My Name Is Jen.</h2>
    <p class="intro__body">I am studying to become an THRIVE-Certified Functional Health Coach. My training involves many science-based practices that improve both our health and how we grow and change as humans. I now have the opportunity to turn that knowledge into practice by coaching actual clients interested in improving their own health and well-being.</p>
  </section>

  <section class="flyer flyer--back">
    <div class="backdrop" role="img" aria-label="Faint background photo of healthy food and a stethoscope"></div>
    <h2 class="benefits__title">Functional health coaches...</h2>
    <ul class="benefits__list">
      <li class="benefits__item"><svg viewBox="0 0 22 22" aria-hidden="true"><rect x="1" y="4" width="17" height="17" fill="none" stroke="#f2f2f2" stroke-width="1.6"/><path d="M5 12l4 4 11-13" fill="none" stroke="#f2f2f2" stroke-width="1.8"/></svg>Leverage your strengths rather than focus on your weaknesses</li>
      <li class="benefits__item"><svg viewBox="0 0 22 22" aria-hidden="true"><rect x="1" y="4" width="17" height="17" fill="none" stroke="#f2f2f2" stroke-width="1.6"/><path d="M5 12l4 4 11-13" fill="none" stroke="#f2f2f2" stroke-width="1.8"/></svg>Support you in finding your own strategies and motivation for change</li>
      <li class="benefits__item"><svg viewBox="0 0 22 22" aria-hidden="true"><rect x="1" y="4" width="17" height="17" fill="none" stroke="#f2f2f2" stroke-width="1.6"/><path d="M5 12l4 4 11-13" fill="none" stroke="#f2f2f2" stroke-width="1.8"/></svg>Provide a judgment-free zone and support your autonomy</li>
      <li class="benefits__item"><svg viewBox="0 0 22 22" aria-hidden="true"><rect x="1" y="4" width="17" height="17" fill="none" stroke="#f2f2f2" stroke-width="1.6"/><path d="M5 12l4 4 11-13" fill="none" stroke="#f2f2f2" stroke-width="1.8"/></svg>Use an experimental mindset to find and develop sustainable habits</li>
      <li class="benefits__item"><svg viewBox="0 0 22 22" aria-hidden="true"><rect x="1" y="4" width="17" height="17" fill="none" stroke="#f2f2f2" stroke-width="1.6"/><path d="M5 12l4 4 11-13" fill="none" stroke="#f2f2f2" stroke-width="1.8"/></svg>Act as your accountability partner as you reach your unique health goals; whether they be improving sleep, diet, fitness, social connection, or reducing stress.</li>
    </ul>
    <div class="fitness" role="img" aria-label="Photo of a yoga mat, sneakers, water bottle and dumbbell on a blue floor"></div>
    <div class="invite">
      <p>I would like to invite you to participate with me as a client as I continue to hone my coaching skills. We can develop a plan and schedule that aligns with your goals.</p>
      <p>As a way to give back to my community, I am offering new clients six free coaching sessions. This is a limited time offer.</p>
    </div>
    <p class="contact__lead">Please contact me.<br>I'm ready to support you as you<br>work to improve your health.</p>
    <div class="contact__band">
      <p class="contact__name">JEN TALVORA</p>
      <p class="contact__line">Call: 555-014-2290 | talvorahwc@example.com</p>
    </div>
    <div class="brand">
      <span class="brand__name">TALVORA</span>
      <span class="brand__tag">HEALTH &amp; WELLNESS COACHING</span>
    </div>
  </section>
</body>
</html>
```